professional business card design

Business card design. Photos have been uploaded and i am open to the designer choosing which photos to use. Would like the card to be mostyly in a grey scale design with black, whites, silver & grey colours. I have added copy of our flyer as would like on the back side of card our services to be listed. Do not use any bright colurs such as blue red green or yellow. i need to be able to edit the phone number and naem in the final card design submitted.

Target Market(s)

Clients

Industry/Entity Type

earhmovibng and transport

Contact Information for Business Card

Director Name, address, email, phone number and services

Colors

Designer to choose only greyscale colors for use in the design.

Requirements
Should not have
• no yellow, red, blue or green

```html
<!DOCTYPE html>
<html lang="en">
<head>
<meta charset="utf-8">
<title>Ridgeway Haulage – Business Card</title>
<link href="https://fonts.googleapis.com/css2?family=Michroma&family=Teko:wght@400;500&family=Open+Sans:wght@600&display=swap" rel="stylesheet">
<style>
  :root {
    --page: #d6d6d6;
    --black: #0b0b0b;
    --charcoal: #2e2e2e;
    --graphite: #454545;
    --steel: #8c8c8c;
    --silver: #c9c9c9;
    --silver-light: #efefef;
    --white: #ffffff;
  }
  * { box-sizing: border-box; margin: 0; padding: 0; }
  html, body { width: 700px; height: 1200px; overflow: hidden; }
  body { background: var(--page); position: relative; font-family: "Michroma", sans-serif; }

  .card {
    position: absolute; left: 0; width: 700px; height: 400px;
    overflow: hidden; background: var(--charcoal);
    box-shadow: 0 6px 18px rgba(0,0,0,.35);
  }
  .card--services { top: 170px; }
  .card--contact { top: 630px; }
  .card-shapes { position: absolute; inset: 0; }

  .services-title {
    position: absolute; top: 22px; right: 26px;
    font-size: 30px; letter-spacing: 1px; color: var(--white);
    -webkit-text-stroke: 1.5px var(--black);
    text-shadow: 2px 2px 0 var(--black);
  }
  .services-list { position: absolute; list-style: none; color: var(--white); font-size: 11.5px; line-height: 19.5px; }
  .services-list li { padding-left: 14px; position: relative; }
  .services-list li::before { content: ""; position: absolute; left: 0; top: 7px; width: 6px; height: 6px; border-radius: 50%; background: var(--white); }
  .services-list--primary { left: 452px; top: 104px; }
  .services-list--secondary { left: 384px; top: 246px; }

  .brand-name {
    position: absolute; left: 40px; top: 140px; width: 240px; text-align: center;
    font-size: 20px; color: var(--silver-light); letter-spacing: 1px;
  }

  .person { position: absolute; left: 376px; top: 10px; width: 254px; text-align: center; }
  .person-name { font-family: "Teko", sans-serif; font-weight: 500; font-size: 46px; line-height: 40px; color: var(--white); -webkit-text-stroke: 1px var(--black); }
  .person-rule { height: 2px; background: var(--black); margin: 2px 0 4px; box-shadow: 0 1px 0 var(--white); }
  .person-role { font-family: "Teko", sans-serif; font-size: 16px; letter-spacing: 4px; color: var(--black); }

  .contact-list { position: absolute; left: 408px; top: 110px; list-style: none; }
  .contact-item { display: flex; align-items: center; gap: 12px; color: var(--white); font-family: "Open Sans", sans-serif; font-weight: 600; font-size: 19px; line-height: 19px; margin-bottom: 16px; }
  .contact-icon { width: 30px; height: 30px; flex: none; }

  .website {
    position: absolute; right: 28px; bottom: 24px;
    font-size: 17px; color: var(--white);
    -webkit-text-stroke: 1px var(--black); text-shadow: 1px 1px 0 var(--black);
  }
</style>
</head>
<body>

<section class="card card--services">
  <svg class="card-shapes" width="700" height="400" viewBox="0 0 700 400">
    <defs>
      <linearGradient id="panelDark" x1="0" y1="0" x2="0" y2="1">
        <stop offset="0" stop-color="#3d3d3d"/><stop offset="1" stop-color="#2a2a2a"/>
      </linearGradient>
      <linearGradient id="bandSilver" x1="0" y1="0" x2="0" y2="1">
        <stop offset="0" stop-color="#f2f2f2"/><stop offset=".5" stop-color="#bdbdbd"/><stop offset="1" stop-color="#7d7d7d"/>
      </linearGradient>
      <radialGradient id="photoDark" cx=".45" cy=".4" r=".7">
        <stop offset="0" stop-color="#3a3a3a"/><stop offset=".6" stop-color="#161616"/><stop offset="1" stop-color="#050505"/>
      </radialGradient>
    </defs>
    <rect width="700" height="400" fill="url(#panelDark)"/>
    <polygon points="184,0 700,0 700,82 296,82" fill="url(#bandSilver)"/>
    <polygon points="0,0 184,0 392,152 304,400 0,400" fill="url(#photoDark)" role="img" aria-label="Road train tipper trucks lined up on a dark metal backdrop"/>
    <polyline points="184,0 392,152 304,400" fill="none" stroke="#b5b5b5" stroke-width="9"/>
    <polyline points="178,-4 386,148 298,400" fill="none" stroke="#555" stroke-width="2"/>
  </svg>
  <div class="brand-name">Ridgeway Haulage</div>
  <h2 class="services-title">OUR SERVICES</h2>
  <ul class="services-list services-list--primary">
    <li>Road Train Tippers</li>
    <li>Road Train Tankers</li>
    <li>Road Train Flat Tops</li>
    <li>Drop Deck Trailers</li>
    <li>Mine Site Accredited<br>Equipment &amp; Operators</li>
  </ul>
  <ul class="services-list services-list--secondary">
    <li>Over Size Loads / Hot Shot Loads</li>
    <li>Heavy Vehicle Recovery Services</li>
    <li>Potable Water Deliveries</li>
    <li>Road Building / Maintenance</li>
    <li>Earthworks</li>
    <li>Sand &amp; Metal Supply &amp; Cartage</li>
  </ul>
</section>

<section class="card card--contact">
  <svg class="card-shapes" width="700" height="400" viewBox="0 0 700 400">
    <defs>
      <linearGradient id="panelDark2" x1="0" y1="0" x2="0" y2="1">
        <stop offset="0" stop-color="#3d3d3d"/><stop offset="1" stop-color="#2a2a2a"/>
      </linearGradient>
      <linearGradient id="bandSilver2" x1="0" y1="0" x2="0" y2="1">
        <stop offset="0" stop-color="#f2f2f2"/><stop offset=".5" stop-color="#bdbdbd"/><stop offset="1" stop-color="#7d7d7d"/>
      </linearGradient>
      <linearGradient id="photoTruck" x1="0" y1="0" x2="0" y2="1">
        <stop offset="0" stop-color="#0a0a0a"/><stop offset=".55" stop-color="#1c1c1c"/><stop offset=".8" stop-color="#6b5a4a"/><stop offset="1" stop-color="#8a7460"/>
      </linearGradient>
    </defs>
    <rect width="700" height="400" fill="url(#panelDark2)"/>
    <polygon points="184,0 700,0 700,82 266,82" fill="url(#bandSilver2)"/>
    <polygon points="328,320 700,320 700,400 304,400" fill="url(#bandSilver2)"/>
    <polygon points="0,0 184,0 368,184 304,400 0,400" fill="url(#photoTruck)" role="img" aria-label="Black road train truck on a red dirt outback road"/>
    <polyline points="184,0 368,184 304,400" fill="none" stroke="#b5b5b5" stroke-width="9"/>
    <polyline points="178,-4 362,180 298,400" fill="none" stroke="#555" stroke-width="2"/>
  </svg>

  <div class="person">
    <div class="person-name">YOUR NAME</div>
    <div class="person-rule"></div>
    <div class="person-role">PROFESSION</div>
  </div>

  <ul class="contact-list">
    <li class="contact-item">
      <svg class="contact-icon" viewBox="0 0 30 30"><circle cx="15" cy="15" r="15" fill="#fff"/><rect x="7.5" y="10" width="15" height="10" rx="1" fill="none" stroke="#2e2e2e" stroke-width="1.8"/><polyline points="7.5,10.5 15,16 22.5,10.5" fill="none" stroke="#2e2e2e" stroke-width="1.8"/></svg>
      <span>Info @email space</span>
    </li>
    <li class="contact-item">
      <svg class="contact-icon" viewBox="0 0 30 30"><circle cx="15" cy="15" r="15" fill="#fff"/><path d="M10.5 8.5l3 3-1.6 2a9 9 0 0 0 4.6 4.6l2-1.6 3 3-2 2.2C14 21.5 8.5 16 8.3 10.5z" fill="#2e2e2e"/></svg>
      <span>+1 123456789<br>+1 123456789</span>
    </li>
    <li class="contact-item">
      <svg class="contact-icon" viewBox="0 0 30 30"><circle cx="15" cy="15" r="15" fill="#fff"/><path d="M15 7a5.5 5.5 0 0 0-5.5 5.5C9.5 17 15 23 15 23s5.5-6 5.5-10.5A5.5 5.5 0 0 0 15 7z" fill="#2e2e2e"/><circle cx="15" cy="12.5" r="2.2" fill="#fff"/></svg>
      <span>123,Dummy,Lorem Ipsum</span>
    </li>
  </ul>

  <div class="website">www.Your_website.com</div>
</section>

</body>
</html>
```